Tarrow Consulting Needs Standardised Stationery!

Hello,I am looking at having some standardised stationery to continue building my brand. I am looking for a relatively clean and simple designs using the colours from my logos. Tarrow Consulting is the main business with Career Beacon Australia a subsidiary.
In particular I am after a design for:
- Letterhead (very important), white background, professional, corporate that I can send to prospective clients. Logo colours.
- Envelope, standard design I can print onto envelopes.
- Pens
- Other stationery/promotional items I can create

Target Market(s)

Universities, government, large organisations.

Industry/Entity Type

Professional Service

Font styles to use
Serif

Requirements
Must have
• Logo, match the design of the Tarrow Consulting logo. Black Career Beacon Australia logo is a subsidiary.
Should not have
• Too much colour, some colour is good, but I am looking for a clean professional look.

```html
<!DOCTYPE html>
<html lang="en">
<head>
<meta charset="utf-8">
<title>Tarrow Consulting – Business Card</title>
<link rel="stylesheet" href="https://fonts.googleapis.com/css2?family=Montserrat:wght@400;700&family=Open+Sans:wght@400;600;700&display=swap">
<style>
  :root {
    --bg: #3a3a3c;
    --card-white: #ffffff;
    --ink: #2b2b2b;
    --ink-soft: #444444;
    --rule: #9a9a9a;
    --green: #12a84a;
    --blue: #0f8fd0;
    --orange: #e8812f;
  }
  * { box-sizing: border-box; margin: 0; padding: 0; }
  html, body { width: 1200px; height: 896px; overflow: hidden; }
  body {
    background: var(--bg);
    font-family: "Open Sans", sans-serif;
    color: var(--ink);
    position: relative;
  }
  .card {
    position: absolute;
    left: 240px;
    width: 720px;
    height: 411px;
    overflow: hidden;
    box-shadow: 0 10px 28px rgba(0,0,0,.45);
  }
  .card--front { top: 24px; background: var(--card-white); }
  .card--back {
    top: 461px;
    background: linear-gradient(35deg, var(--blue) 0%, #07a37a 30%, var(--green) 55%, #6aa83e 75%, var(--orange) 100%);
  }

  /* Front */
  .contact { position: absolute; left: 52px; top: 96px; }
  .contact__name {
    font-family: "Montserrat", sans-serif;
    font-weight: 700;
    font-size: 30px;
    letter-spacing: .5px;
    color: var(--green);
    text-transform: uppercase;
    line-height: 1.1;
  }
  .contact__role { font-size: 18px; color: var(--ink-soft); margin-bottom: 14px; }
  .contact__line { display: flex; align-items: center; gap: 8px; font-size: 17px; line-height: 1.45; color: var(--ink); }
  .contact__line svg { width: 15px; height: 15px; fill: var(--green); flex: none; }

  .rule { position: absolute; left: 40px; top: 268px; width: 400px; height: 1px; background: var(--rule); }

  .brand { position: absolute; right: 60px; top: 110px; text-align: left; }
  .brand__name {
    font-family: "Montserrat", sans-serif;
    font-weight: 700;
    font-size: 46px;
    color: var(--ink);
    letter-spacing: 2px;
    line-height: 1;
  }
  .brand__tag {
    font-family: "Montserrat", sans-serif;
    font-weight: 400;
    font-size: 15px;
    color: var(--ink-soft);
    letter-spacing: 11px;
    margin-top: 6px;
  }

  .subbrand { position: absolute; left: 440px; top: 250px; }
  .subbrand__mark { display: flex; align-items: center; gap: 10px; }
  .subbrand__dot { width: 30px; height: 30px; border-radius: 50%; background: var(--ink); flex: none; }
  .subbrand__name { font-family: "Open Sans", sans-serif; font-weight: 700; font-size: 19px; color: var(--ink); line-height: 1.15; }
  .subbrand__address { margin-top: 12px; font-size: 17px; line-height: 1.4; color: var(--ink); }

  .band { position: absolute; left: 0; bottom: 0; width: 100%; height: 10px; display: flex; }
  .band__blue { flex: 25; background: var(--blue); }
  .band__green { flex: 30; background: var(--green); }
  .band__orange { flex: 45; background: var(--orange); }

  /* Back */
  .back-brand { position: absolute; left: 230px; top: 140px; color: #fff; }
  .back-brand .brand__name { color: #fff; font-size: 54px; }
  .back-brand .brand__tag { color: #fff; font-size: 17px; letter-spacing: 13px; }
  .back-web {
    position: absolute; left: 230px; top: 290px;
    color: #fff; font-size: 19px; font-weight: 600; letter-spacing: .5px;
  }
</style>
</head>
<body>

<section class="card card--front">
  <div class="contact">
    <div class="contact__name">Daniel Hartley</div>
    <div class="contact__role">Managing Director</div>
    <div class="contact__line">
      <svg viewBox="0 0 16 16" aria-hidden="true"><path d="M3 1h3l1.5 4-2 1.2a9 9 0 0 0 4.3 4.3L11 8.5l4 1.5v3a2 2 0 0 1-2 2A13 13 0 0 1 1 3a2 2 0 0 1 2-2z"/></svg>
      055-240 318 672
    </div>
    <div class="contact__line">
      <svg viewBox="0 0 16 16" aria-hidden="true"><path d="M4 0h8a1 1 0 0 1 1 1v14a1 1 0 0 1-1 1H4a1 1 0 0 1-1-1V1a1 1 0 0 1 1-1zm1 2v10h6V2H5zm3 11a1 1 0 1 0 0 2 1 1 0 0 0 0-2z"/></svg>
      055-240 318 672
    </div>
    <div class="contact__line">
      <svg viewBox="0 0 16 16" aria-hidden="true"><path d="M0 3h16v10H0V3zm1.5 1.2L8 9l6.5-4.8V4h-13v.2z"/></svg>
      hello@tarrowconsult.com
    </div>
  </div>

  <div class="rule"></div>

  <div class="brand">
    <div class="brand__name">TARROW</div>
    <div class="brand__tag">CONSULTING</div>
  </div>

  <div class="subbrand">
    <div class="subbrand__mark">
      <span class="subbrand__dot"></span>
      <span class="subbrand__name">Career Beacon Australia</span>
    </div>
    <div class="subbrand__address">48 Harbour Lane,<br>Kirrawee NSW, 2232</div>
  </div>

  <div class="band">
    <span class="band__blue"></span>
    <span class="band__green"></span>
    <span class="band__orange"></span>
  </div>
</section>

<section class="card card--back">
  <div class="back-brand">
    <div class="brand__name">TARROW</div>
    <div class="brand__tag">CONSULTING</div>
  </div>
  <div class="back-web">www.tarrowconsult.com</div>
</section>

</body>
</html>
```